Local Flower Farm Needs Business Card Design

I need business cards designed for a flower farm based in Eudora, Kansas.
Business Info:
We are a local cut flower farm located in Eudora, Kansas, founded by Darla Hoffstrom. What started as a passion for agriculture and search for more joy in daily life has blossomed into a small business dedicated to providing the community with beautiful, fresh, and sustainable flowers. We specialize in local, seasonal blooms, ensuring that every petal reflects the care and dedication we pour into our craft. Our mission is to deliver the highest quality flowers directly to our customers through local farmers markets and to florists who share our commitment to sustainability. Join us in celebrating the beauty of nature, one bloom at a time!
Contact Details:
Darla Hoffstrom
Owner
Phone 913-555-0147
Facebook: Lorabelle Quinn Blossoms
Instagram: @LorabelleQuinnBlossoms
Website: LorabelleQuinnBlossoms.example
Target Market(s)
Wholesale to Florists and Direct to Consumer via Farmers Market
Industry/Entity Type
Florist, Farm
Contact Information for Business Card
Name, Contact Info, Logo
Look and feel

```html
<!DOCTYPE html>
<html lang="en">
<head>
<meta charset="utf-8">
<title>Lorabelle Quinn Blossoms – Business Card</title>
<link href="https://fonts.googleapis.com/css2?family=Montserrat:wght@500;600;700&display=swap" rel="stylesheet">
<style>
  :root {
    --page-bg: #dedede;
    --forest: #06272d;
    --paper: #ffffff;
    --grey-text: #6f6f6f;
    --rule: #8a8a8a;
  }
  html, body {
    margin: 0;
    padding: 0;
    width: 1200px;
    height: 1200px;
    overflow: hidden;
    background: var(--page-bg);
    font-family: "Montserrat", Arial, sans-serif;
  }
  .canvas {
    position: relative;
    width: 1200px;
    height: 1200px;
  }
  .card {
    position: absolute;
    left: 179px;
    width: 861px;
    height: 496px;
  }
  .card-front { top: 84px; background: var(--forest); }
  .card-back { top: 621px; background: var(--paper); }

  .brand-seal {
    position: absolute;
    border-radius: 50%;
    display: flex;
    align-items: center;
    justify-content: center;
    text-align: center;
    box-sizing: border-box;
  }
  .brand-seal .brand-name {
    font-family: "Montserrat", Arial, sans-serif;
    font-weight: 600;
    text-transform: uppercase;
    letter-spacing: 3px;
    line-height: 1.5;
  }
  .card-front .brand-seal {
    left: 289px; top: 125px;
    width: 230px; height: 230px;
    border: 1px solid var(--paper);
  }
  .card-front .brand-name { color: var(--paper); font-size: 17px; }
  .card-back .brand-seal {
    left: 119px; top: 160px;
    width: 174px; height: 174px;
    border: 1px solid var(--forest);
  }
  .card-back .brand-name { color: var(--forest); font-size: 13px; letter-spacing: 2px; }

  .divider {
    position: absolute;
    left: 321px; top: 152px;
    width: 1px; height: 193px;
    background: var(--rule);
  }
  .contact-block {
    position: absolute;
    left: 340px; top: 144px;
  }
  .person-name {
    margin: 0;
    font-size: 30px;
    font-weight: 700;
    color: var(--forest);
    line-height: 1.1;
    letter-spacing: 0.3px;
  }
  .person-role {
    margin: 0 0 10px;
    font-size: 24px;
    font-weight: 500;
    color: var(--grey-text);
    line-height: 1.2;
    letter-spacing: 0.5px;
  }
  .contact-list { list-style: none; margin: 0; padding: 0; }
  .contact-item {
    display: flex;
    align-items: center;
    height: 35px;
    font-size: 17px;
    font-weight: 600;
    color: var(--grey-text);
    letter-spacing: 1.4px;
  }
  .contact-icon {
    width: 20px; height: 20px;
    margin-right: 14px;
    flex: none;
  }
</style>
</head>
<body>
<main class="canvas">
  <section class="card card-front" aria-label="Card front">
    <div class="brand-seal">
      <span class="brand-name">Lorabelle<br>Quinn<br>Blossoms</span>
    </div>
  </section>

  <section class="card card-back" aria-label="Card back">
    <div class="brand-seal">
      <span class="brand-name">Lorabelle<br>Quinn<br>Blossoms</span>
    </div>
    <div class="divider"></div>
    <div class="contact-block">
      <h1 class="person-name">Darla Hoffstrom</h1>
      <p class="person-role">Owner</p>
      <ul class="contact-list">
        <li class="contact-item">
          <svg class="contact-icon" viewBox="0 0 20 20" aria-hidden="true">
            <rect width="20" height="20" fill="#06272d"/>
            <path d="M7 4 L9 4 L9.5 7 L8 8 Q9 11.5 12 13 L13 11.5 L16 12 L16 14 Q15 16 13 16 Q6 14 4.5 7 Q4.5 4.5 7 4 Z" fill="#ffffff"/>
          </svg>
          913-555-0147
        </li>
        <li class="contact-item">
          <svg class="contact-icon" viewBox="0 0 20 20" aria-hidden="true">
            <rect width="20" height="20" fill="#06272d"/>
          </svg>
          @LorabelleQuinnBlossoms
        </li>
        <li class="contact-item">
          <svg class="contact-icon" viewBox="0 0 20 20" aria-hidden="true">
            <rect x="1" y="1" width="18" height="18" fill="none" stroke="#06272d" stroke-width="2"/>
          </svg>
          @LorabelleQuinnBlossoms
        </li>
        <li class="contact-item">
          <svg class="contact-icon" viewBox="0 0 20 20" aria-hidden="true">
            <rect width="20" height="20" fill="#06272d"/>
            <circle cx="10" cy="10" r="6" fill="none" stroke="#ffffff" stroke-width="1.5"/>
            <path d="M4 10 H16 M10 4 Q6.5 10 10 16 M10 4 Q13.5 10 10 16" fill="none" stroke="#ffffff" stroke-width="1.2"/>
          </svg>
          LorabelleQuinnBlossoms.example
        </li>
      </ul>
    </div>
  </section>
</main>
</body>
</html>
```